Ecommerce web site design for 80s Retro website

we need a website to sell retro gift boxes based around 80's movies, music and gaming
it needs to work with the cartvella ecommerce provider
there would only be 3 basic gift boxes (music, movies and gaming) , but the packaging would be able to be chosen to match birthdays, Christmas etc.
Each themed box will also have three levels of pricing, classic, premium, ultimate.
the website should be themed around the same colour scheme and look as the logo.

Target Market(s)

People after retro presents and gifts so probably people in their 40s to 50s

Coding

Coded - Design and coding required

Number of Pages Required

1 page

Requirements
Must have
• A real retro look and feel with bright neon colours and some icons or symbols of things from the 80s like walkmans, joysticks, movies, music, gaming etc
Should not have
• A boring bland interface

```html
<!DOCTYPE html>
<html lang="en">
<head>
<meta charset="utf-8">
<title>Neon Attic – Retro Gift Boxes</title>
<link rel="stylesheet" href="https://fonts.googleapis.com/css2?family=Bungee&family=Great+Vibes&family=Poppins:wght@400;500;600;700&family=Zilla+Slab:wght@600;700&display=swap">
<style>
:root{
  --pink:#e8479c;
  --pink-soft:#fbe4ec;
  --purple:#9b59d6;
  --violet:#7b4fe0;
  --blue:#3d7cf0;
  --ink:#111014;
  --dark:#060506;
  --white:#ffffff;
  --text:#3a3340;
  --grey:#e6e4e4;
}
*{margin:0;padding:0;box-sizing:border-box}
html,body{width:1200px;height:3834px;overflow:hidden}
body{position:relative;font-family:'Poppins',sans-serif;color:var(--text);background:var(--pink-soft)}
.abs{position:absolute}
.script{font-family:'Great Vibes',cursive}
.display{font-family:'Bungee',sans-serif}
.slab{font-family:'Zilla Slab',serif}

/* header */
.topbar{left:0;top:0;width:1200px;height:112px;background:linear-gradient(180deg,#c25fc7 0%,#9d6bd0 100%)}
.brand{left:150px;top:36px;display:flex;align-items:center;gap:10px;font-weight:700;font-size:22px;color:var(--white);letter-spacing:1px}
.brand i{width:16px;height:16px;border-radius:50%;background:var(--white);display:block}
.search{left:368px;top:30px;width:461px;height:41px;background:var(--white);border-radius:21px;border:3px solid #b57bd6;font-size:11px;color:#aaa;padding:11px 20px}
.search b{position:absolute;right:2px;top:2px;width:58px;height:31px;border-radius:16px;background:#222}
.signin{left:847px;top:37px;color:var(--white);font-style:italic;font-size:13px;font-family:'Zilla Slab',serif}
.cart-ic{left:901px;top:28px;width:42px;height:42px;border-radius:50%;border:2px solid rgba(255,255,255,.7)}
.cart-txt{left:952px;top:30px;color:var(--white);font-size:10px;line-height:15px}
.cart-txt em{font-family:'Zilla Slab',serif;font-size:13px}
.nav{left:0;top:112px;width:1200px;height:38px;background:linear-gradient(90deg,#ec4a9c,#c45fd0 50%,#9c6ae0)}
.nav span,.foot-nav span{position:absolute;top:11px;transform:translateX(-50%);font-family:'Bungee',sans-serif;font-size:13px;color:var(--white)}

/* hero */
.hero{left:0;top:150px;width:1200px;height:457px;background:var(--grey);overflow:hidden}
.hero-photo{left:417px;top:0;width:783px;height:457px;background:linear-gradient(90deg,rgba(230,228,228,0),#a9a09a 30%,#7c6a5e 60%,#b7aca6)}
.hero-ring{left:-140px;top:100px;width:550px;height:550px;border-radius:50%;border:7px solid #b35ccf}
.badge{left:326px;top:267px;width:110px;height:110px;border-radius:50%;background:linear-gradient(135deg,var(--pink),var(--violet));border:3px solid var(--white);color:var(--white);text-align:center;padding-top:18px}
.badge small{font-size:13px;display:block}
.badge strong{font-family:'Bungee',sans-serif;font-size:34px;line-height:38px}
.badge span{font-size:11px;display:block;font-weight:600}
.save{left:95px;top:365px;font-size:48px;color:#2c2530}
.seventy{left:160px;top:420px;font-family:'Bungee',sans-serif;font-style:italic;font-size:62px;color:var(--blue)}
.btn{display:flex;align-items:center;justify-content:center;border-radius:26px;color:var(--white);font-family:'Zilla Slab',serif;font-weight:700;letter-spacing:.5px;background:linear-gradient(90deg,#ee4691,#b456d8)}
.explore{left:98px;top:511px;width:207px;height:46px;font-size:17px}

/* collection */
.collection{left:0;top:607px;width:1200px;height:923px;background:radial-gradient(ellipse at center,#fff4f7 55%,#efd5dc 100%)}
.card{border-radius:22px;box-shadow:0 8px 14px rgba(0,0,0,.2);overflow:hidden}
.card-music{left:149px;top:677px;width:528px;height:443px;background:linear-gradient(90deg,#7c6a4e 0%,#8a8a80 40%,#4f8ff0 65%,#2e6fe0)}
.card-gaming{left:697px;top:677px;width:351px;height:216px;background:linear-gradient(90deg,#b49072 0%,#c68fa0 55%,#ee4fa8)}
.card-movies{left:697px;top:904px;width:351px;height:216px;background:linear-gradient(90deg,#8a6e62 0%,#b06aa8 55%,#d44fb8)}
.disc-label{left:480px;top:868px;color:var(--white);text-align:left}
.disc-label .script{font-size:34px;display:block;margin-left:40px}
.disc-label .display{font-size:44px;line-height:52px;display:block}
.disc-label .display.big{font-size:58px;line-height:62px}
.vert{left:990px;top:700px;width:20px;font-family:'Bungee',sans-serif;font-size:22px;line-height:27px;color:var(--white);text-align:center}
.year{font-family:'Bungee',sans-serif;font-style:italic;color:var(--white);font-size:28px}
.collect-badge{left:603px;top:628px;width:134px;height:134px;border-radius:50%;background:linear-gradient(135deg,var(--pink),var(--violet));border:3px solid var(--white);color:var(--white);text-align:center;padding-top:32px}
.collect-badge .script{font-size:26px;line-height:24px;display:block}
.collect-badge .display{font-size:17px;display:block}
.collect-badge small{font-size:9px;line-height:11px;display:block}
.welcome{left:0;top:1146px;width:1200px;text-align:center}
.welcome .script{font-size:48px;color:var(--blue);line-height:48px;display:block}
.welcome .display{font-size:46px;color:var(--pink);line-height:56px}
.rule{top:1221px;height:0;border-top:1px dashed #9a909a;width:140px}
.intro{left:200px;top:1274px;width:800px;text-align:center;font-size:11.5px;line-height:17.5px;color:#4a4450}
.readmore{left:496px;top:1365px;width:208px;height:49px;font-size:17px}

/* categories */
.cats{left:0;top:1530px;width:1200px;height:331px;background:radial-gradient(circle at 15% 30%,#201c20,var(--dark) 45%),var(--dark)}
.cat{width:330px;text-align:center;color:var(--white)}
.cat-ic{width:176px;height:176px;border-radius:50%;background:linear-gradient(150deg,var(--violet),var(--pink));border:5px solid #e9e3ee;margin:0 auto;display:flex;align-items:center;justify-content:center}
.cat .script{font-size:40px;margin-top:12px;line-height:50px}
.cat p{font-size:12px;line-height:18px;width:250px;margin:6px auto 0}
.cat .go{width:16px;height:16px;border-radius:50%;background:var(--pink);margin:12px auto 0}

/* products */
.products{left:0;top:1861px;width:1200px;height:934px;background:linear-gradient(100deg,#f1e6f1,#fdf2f5 50%,#fbe0ea)}
.prod-head{left:0;top:1805px;width:603px;height:104px;background:var(--pink);border-radius:0 55px 55px 0;box-shadow:3px 3px 0 #fff,5px 5px 0 var(--pink)}
.prod-head h2{position:absolute;left:149px;top:18px;font-family:'Bungee',sans-serif;font-weight:400;font-size:38px;color:var(--white)}
.prod-head nav{position:absolute;left:149px;top:70px;font-family:'Zilla Slab',serif;font-size:15px;color:var(--white)}
.prod-head nav span{margin-right:34px}
.prod{width:291px;text-align:center}
.prod .ph{height:273px}
.prod .name{font-size:24px;color:#2c2530;margin-top:12px;line-height:26px}
.prod .price{font-family:'Bungee',sans-serif;font-style:italic;font-size:17px;color:#2c2530;line-height:24px}
.prod .add{width:170px;height:45px;margin:10px auto 0;border:2px solid var(--pink);border-radius:23px;font-family:'Zilla Slab',serif;font-weight:700;font-size:16px;color:#2c2530;line-height:41px;background:var(--white)}

/* blog */
.blog{left:0;top:2795px;width:1200px;height:682px;background:var(--dark)}
.blog-title{left:0;top:2852px;width:1200px;text-align:center;font-family:'Bungee',sans-serif;font-size:46px;color:var(--white)}
.blog-rule{top:2878px;border-top:1px dashed #777;width:160px}
.post{left:149px;width:292px;color:var(--white)}
.post h3{font-family:'Great Vibes',cursive;font-weight:400;font-size:30px;line-height:34px}
.post .meta{display:flex;justify-content:space-between;font-size:11px;margin-top:8px}
.post p{font-size:11px;line-height:17px;margin-top:7px}
.post a{font-size:11px;color:var(--pink);text-decoration:underline}
.blog-photo{left:500px;top:2993px;width:548px;height:408px;border-radius:22px;background:radial-gradient(circle at 55% 55%,#c79a3a,#6b5a2a 55%,#2c2818)}
.arrow-btn{top:3350px;width:30px;height:30px;border-radius:50%;border:2px solid var(--pink);color:var(--white);font-size:14px;text-align:center;line-height:26px}

/* footer */
.footer{left:0;top:3477px;width:1200px;height:317px;background:#0b0a0c}
.foot-brand{left:0;top:3535px;width:1200px;display:flex;justify-content:center;align-items:center;gap:12px;font-weight:700;font-size:30px;color:var(--white);letter-spacing:1px}
.foot-brand i{width:20px;height:20px;border-radius:50%;background:var(--pink);display:block}
.social{top:3642px;width:42px;height:42px;border-radius:50%;border:2px solid var(--pink)}
.email{left:384px;top:3633px;width:466px;height:57px;border-radius:29px;background:var(--white);font-size:11px;color:#999;padding:21px 26px}
.submit{left:698px;top:3640px;width:146px;height:43px;font-size:19px;border-radius:22px;background:linear-gradient(90deg,#d945c8,#7b4fe0)}
.phone-ic{left:865px;top:3642px;width:42px;height:42px;border-radius:50%;border:2px solid var(--pink);display:flex;align-items:center;justify-content:center}
.phone{left:918px;top:3655px;font-size:13px;color:var(--white);font-weight:500}
.foot-nav{left:0;top:3722px;width:1200px;height:30px}
.copy{left:0;top:3794px;width:1200px;height:40px;background:linear-gradient(90deg,#ea4a9e,#a461d8);color:var(--white);font-size:11px;text-align:center;line-height:40px}
</style>
</head>
<body>

<!-- header -->
<header class="abs topbar"></header>
<div class="abs brand"><i></i>NEON ATTIC</div>
<div class="abs search">Search your product<b></b>
  <svg class="abs" style="right:23px;top:11px" width="14" height="14" viewBox="0 0 14 14"><circle cx="6" cy="6" r="4.5" fill="none" stroke="#fff" stroke-width="2"/><line x1="9.5" y1="9.5" x2="13" y2="13" stroke="#fff" stroke-width="2"/></svg>
</div>
<div class="abs signin">Sign In</div>
<div class="abs cart-ic">
  <svg width="38" height="38" viewBox="0 0 38 38"><path d="M11 14h16l-2 10H13z" fill="none" stroke="#fff" stroke-width="1.6"/><path d="M15 14v-3h8v3" fill="none" stroke="#fff" stroke-width="1.6"/></svg>
</div>
<div class="abs cart-txt"><em>Shipping Cart</em><br>0 Cart Subtotal : $00</div>
<nav class="abs nav">
  <span style="left:259px">MOVIE</span><span style="left:377px">MUSIC</span><span style="left:500px">GAMING</span><span style="left:643px">TODAYS DEALS</span><span style="left:800px">GIFT CARDS</span><span style="left:935px">PRICING</span>
</nav>

<!-- hero -->
<section class="abs hero">
  <div class="abs hero-photo" role="img" aria-label="Vintage room with radio, teddy bear, violin, gramophone and retro telephone"></div>
  <div class="abs hero-ring" style="top:100px"></div>
</section>
<div class="abs badge"><small>ANY 5</small><strong>$25</strong><span>Product</span></div>
<div class="abs save script">Save up to</div>
<div class="abs seventy">70%</div>
<div class="abs btn explore">EXPLORE NOW&nbsp;
  <svg width="22" height="12" viewBox="0 0 22 12"><path d="M0 6h20M15 1l5 5-5 5" fill="none" stroke="#fff" stroke-width="2"/></svg>
</div>

<!-- collection -->
<section class="abs collection"></section>
<div class="abs card card-music" role="img" aria-label="Man with headphones sharing music with a friend"></div>
<div class="abs disc-label"><span class="script">Discount</span><span class="display">25 %</span><span class="display big">MUSIC</span></div>
<div class="abs card card-gaming" role="img" aria-label="Boombox and cassette tapes on wooden floor"></div>
<div class="abs year" style="left:898px;top:760px">2022</div>
<div class="abs vert">G A M I N G</div>
<div class="abs card card-movies" role="img" aria-label="Shop keeper in a record and movie store"></div>
<div class="abs year" style="left:912px;top:1013px">2022</div>
<div class="abs display" style="left:912px;top:1043px;font-size:32px;color:#fff">MOVIES</div>
<div class="abs collect-badge"><span class="script">Best</span><span class="display">COLLECTION</span><small>Music, Movies and<br>Gaming</small></div>

<div class="abs welcome"><span class="script">Welcome to</span><span class="display">NEON ATTIC</span></div>
<div class="abs rule" style="left:318px"></div>
<div class="abs rule" style="left:740px"></div>
<p class="abs intro">Lorem ipsum dolor sit amet, consectetur adipiscing elit. Morbi ut urna mauris. Nunc eget malesuada turpis, a ornare lorem. Integer euismod consectetur mattis. In erat sapien, faucibus ac nibh et, posuere finibus tortor. Cras efficitur in odio eu posuere. Morbi sed tortor auctor, ultrices neque et, porta nulla. Nam fringilla est a dui feugiat pharetra. Quisque consectetur pharetra pharetra. Nam mauris eros, consectetur id condimentum in</p>
<div class="abs btn readmore">READ MORE&nbsp;➜</div>

<!-- categories -->
<section class="abs cats"></section>
<div class="abs cat" style="left:110px;top:1458px">
  <div class="cat-ic"><svg width="80" height="80" viewBox="0 0 80 80" fill="none" stroke="#fff" stroke-width="4"><path d="M20 50V18l20-4v30"/><circle cx="15" cy="50" r="6"/><circle cx="35" cy="44" r="6"/><path d="M54 64V40l16-4v24"/><circle cx="50" cy="64" r="5"/><circle cx="66" cy="60" r="5"/><path d="M56 16v10M51 21h10M32 60v8M28 64h8"/></svg></div>
  <div class="script">Music</div><p>Lorem ipsum dolor sit amet, consectetur adipiscing elit. Vestibulum</p><div class="go"></div>
</div>
<div class="abs cat" style="left:441px;top:1458px">
  <div class="cat-ic"><svg width="96" height="70" viewBox="0 0 96 70" fill="none" stroke="#fff" stroke-width="5"><path d="M20 10h56c10 0 16 10 16 28s-6 28-14 28c-8 0-12-12-18-12H36c-6 0-10 12-18 12C10 66 4 56 4 38S10 10 20 10z"/><path d="M26 28v18M17 37h18"/><circle cx="66" cy="32" r="3" fill="#fff"/><circle cx="74" cy="42" r="3" fill="#fff"/></svg></div>
  <div class="script">Game</div><p>Lorem ipsum dolor sit amet, consectetur adipiscing elit. Vestibulum</p><div class="go"></div>
</div>
<div class="abs cat" style="left:770px;top:1458px">
  <div class="cat-ic"><svg width="80" height="70" viewBox="0 0 80 70" fill="none" stroke="#fff" stroke-width="5"><rect x="6" y="8" width="68" height="54" rx="6"/><path d="M6 22h68M18 8l-6 14M32 8l-6 14M46 8l-6 14M60 8l-6 14"/><path d="M33 32l16 10-16 10z" fill="#fff"/></svg></div>
  <div class="script">Movie</div><p>Lorem ipsum dolor sit amet, consectetur adipiscing elit. Vestibulum</p><div class="go"></div>
</div>

<!-- products -->
<section class="abs products"></section>
<div class="abs prod-head"><h2>OUR PRODUCT</h2><nav><span>ALL MUSIC</span><span>MOVIES</span><span>GAMING</span></nav></div>

<div class="abs prod" style="left:150px;top:1942px"><div class="ph" role="img" aria-label="Vintage transistor radio on orange background" style="background:linear-gradient(180deg,#f2a31c,#e89420 70%,#d9b99a)"></div><div class="name script">Lorem Ipsum</div><div class="price">$ 220</div><div class="add">ADD TO CART</div></div>
<div class="abs prod" style="left:456px;top:1942px"><div class="ph" role="img" aria-label="Antique gramophone on a wooden stand" style="background:radial-gradient(circle at 55% 50%,#8a6b4a,#9d9893 40%,#c7c4c0)"></div><div class="name script">Lorem Ipsum</div><div class="price">$ 120</div><div class="add">ADD TO CART</div></div>
<div class="abs prod" style="left:761px;top:1942px"><div class="ph" role="img" aria-label="Record player with a red label vinyl" style="background:radial-gradient(circle at 50% 42%,#1a1a1a 30%,#8e8a86 32%,#b3b0ac)"></div><div class="name script">Lorem Ipsum</div><div class="price">$ 225</div><div class="add">ADD TO CART</div></div>
<div class="abs prod" style="left:150px;top:2348px"><div class="ph" role="img" aria-label="Pink portable turntable with records" style="background:linear-gradient(160deg,#9fa1a4,#c9a3a6 50%,#e0b8b8)"></div><div class="name script">Lorem Ipsum</div><div class="price">$ 200</div><div class="add">ADD TO CART</div></div>
<div class="abs prod" style="left:456px;top:2348px"><div class="ph" role="img" aria-label="Close view of a black vinyl record on a turntable" style="background:radial-gradient(circle at 60% 40%,#3a3836,#1b1a19 55%,#b9b3aa)"></div><div class="name script">Lorem Ipsum</div><div class="price">$ 250</div><div class="add">ADD TO CART</div></div>
<div class="abs prod" style="left:761px;top:2348px"><div class="ph" role="img" aria-label="Silver boombox on a wooden table against teal wall" style="background:linear-gradient(180deg,#2d8d8a,#4fa3a0 55%,#b47b4c)"></div><div class="name script">Lorem Ipsum</div><div class="price">$ 320</div><div class="add">ADD TO CART</div></div>

<!-- blog -->
<section class="abs blog"></section>
<div class="abs blog-title">OUR BLOG</div>
<div class="abs blog-rule" style="left:300px"></div>
<div class="abs blog-rule" style="left:742px"></div>

<article class="abs post" style="top:3015px">
  <h3>In ultrices Porttitor Risus</h3>
  <div class="meta"><span>▦ Date 02.03.22</span><span>● 32</span></div>
  <p>vitae posuere nisl. In a nisl vitae odio mattis fringilla. Mauris in nulla ut tellus ultricies commodo. Mauris eu sagittis nulla. Aenean eu consequat</p>
  <a>Read More &gt;</a>
</article>
<article class="abs post" style="top:3190px">
  <h3>In ultrices Porttitor Risus</h3>
  <div class="meta"><span>▦ Date 02.03.22</span><span>● 32</span></div>
  <p>vitae posuere nisl. In a nisl vitae odio mattis fringilla. Mauris in nulla ut tellus ultricies commodo. Mauris eu sagittis nulla. Aenean eu consequat</p>
  <a>Read More &gt;</a>
</article>
<div class="abs arrow-btn" style="left:372px">‹</div>
<div class="abs arrow-btn" style="left:409px">›</div>
<div class="abs blog-photo" role="img" aria-label="Man in yellow shirt with red headphones dancing on a sofa"></div>

<!-- footer -->
<footer class="abs footer"></footer>
<div class="abs foot-brand"><i></i>NEON ATTIC</div>
<div class="abs social" style="left:179px" aria-label="Social link"></div>
<div class="abs social" style="left:225px" aria-label="Social link"></div>
<div class="abs social" style="left:271px" aria-label="Social link"></div>
<div class="abs email">ENTER YOUR EMAIL ID</div>
<div class="abs btn submit">SUBMIT</div>
<div class="abs phone-ic"><svg width="16" height="16" viewBox="0 0 16 16"><path d="M3 1l3 3-1.5 2c1 2 3 4 5 5L11.5 9.5l3 3L13 15C7 14 2 9 1 3z" fill="#fff"/></svg></div>
<div class="abs phone">555-014-2297</div>
<nav class="abs foot-nav">
  <span style="left:259px">MOVIE</span><span style="left:377px">MUSIC</span><span style="left:500px">GAMING</span><span style="left:643px">TODAYS DEALS</span><span style="left:800px">GIFT CARDS</span><span style="left:935px">PRICING</span>
</nav>
<div class="abs copy">COPYRIGHT © 2022 NEON ATTIC - ALL RIGHTS RESERVED.</div>

</body>
</html>
```